Tovane and Partners Business Card

A business card that can be templates for all employees using our newly created logo and information. We are looking for stylish however simplistic in nature, clean looks are better than over the top, however creativity will be appreciated if it has the right appeal. Note: If you feel a type of card (plastic, metalic, carbon, raised lettering, etc) helps your design please specify.
Target Market(s)
Investigation ETC
Industry/Entity Type
Private Investigator
Contact Information for Business Card
Dan Moskel
President
5173 Wexmoor Lane
Hermitage PA 16203-4419
Cell: 724-555-0193; Office: 724-555-0147
Email: danmoskel@tovanepartners-example.com
Requirements
Must have
- Website TovanePartners-example.com
- Name, address, phone number ETC
- Use of current Logo and color pallets if applicable
- TM By logo, small

Nice to have
- Would like to see with and without a photo on the design

Should not have
- Redesign of logo, changing of colors

```html
<!DOCTYPE html>
<html lang="en">
<head>
<meta charset="utf-8">
<title>Tovane and Partners Business Card</title>
<link rel="stylesheet" href="https://fonts.googleapis.com/css2?family=Tinos:wght@400;700&family=Arimo:wght@400;500;600;700&display=swap">
<style>
  :root {
    --page: #f1f0ee;
    --card-edge: #dcdbe0;
    --card-face: #ebebed;
    --brand-purple: #351c66;
    --ink: #111111;
    --on-purple: #ffffff;
  }
  html, body {
    margin: 0;
    padding: 0;
    width: 1189px;
    height: 1200px;
    overflow: hidden;
    background: var(--page);
  }
  .canvas {
    position: relative;
    width: 1189px;
    height: 1200px;
  }
  .card {
    position: absolute;
    left: 140px;
    width: 917px;
    height: 524px;
    background: var(--card-edge);
    overflow: hidden;
  }
  .card-front { top: 45px; }
  .card-back { top: 623px; }

  .front-panel {
    position: absolute;
    left: 42px;
    top: 40px;
    width: 832px;
    height: 444px;
    background: var(--card-face);
  }
  .front-frame {
    position: absolute;
    left: 0;
    top: 0;
    width: 917px;
    height: 524px;
  }
  .footer-band {
    position: absolute;
    left: 55px;
    top: 467px;
    width: 806px;
    height: 57px;
    background: var(--brand-purple);
    display: flex;
    align-items: center;
    justify-content: center;
    gap: 34px;
    font-family: "Arimo", Arial, sans-serif;
    font-size: 18px;
    color: var(--on-purple);
    white-space: nowrap;
  }
  .footer-sep {
    width: 1px;
    height: 22px;
    background: var(--on-purple);
  }
  .company-name {
    position: absolute;
    left: 0;
    width: 917px;
    margin: 0;
    text-align: center;
    font-family: "Tinos", "Times New Roman", serif;
    font-weight: 700;
    line-height: 1;
    white-space: nowrap;
  }
  .trademark {
    font-family: "Arimo", Arial, sans-serif;
    font-weight: 400;
    font-size: 14px;
    vertical-align: top;
    margin-left: 3px;
    position: relative;
    top: 4px;
  }
  .card-back .trademark {
    font-size: 17px;
    top: 6px;
  }
  .card-front .company-name {
    top: 106px;
    font-size: 59px;
    color: var(--brand-purple);
  }
  .card-back .company-name {
    top: 221px;
    font-size: 74px;
    color: var(--ink);
  }
  .person {
    position: absolute;
    right: 504px;
    top: 252px;
    text-align: right;
    color: var(--ink);
  }
  .person-name {
    margin: 0;
    font-family: "Tinos", "Times New Roman", serif;
    font-weight: 700;
    font-size: 37px;
    line-height: 1;
  }
  .person-title {
    margin: 4px 0 0;
    font-family: "Arimo", Arial, sans-serif;
    font-weight: 600;
    font-size: 28px;
    line-height: 1;
  }
  .divider {
    position: absolute;
    left: 458px;
    top: 228px;
    width: 2px;
    height: 123px;
    background: var(--ink);
  }
  .contact-list {
    position: absolute;
    left: 501px;
    top: 256px;
    margin: 0;
    padding: 0;
    list-style: none;
    font-family: "Arimo", Arial, sans-serif;
    font-size: 23px;
    color: var(--ink);
  }
  .contact-item {
    display: flex;
    align-items: center;
    height: 36px;
  }
  .contact-icon {
    width: 20px;
    height: 20px;
    margin-right: 31px;
  }
  .address {
    position: absolute;
    left: 0;
    top: 428px;
    width: 917px;
    margin: 0;
    text-align: center;
    font-family: "Arimo", Arial, sans-serif;
    font-size: 22px;
    color: var(--ink);
    line-height: 1;
  }
</style>
</head>
<body>
<main class="canvas">
  <section class="card card-front" aria-label="Card front">
    <div class="front-panel"></div>
    <svg class="front-frame" viewBox="0 0 917 524" aria-hidden="true">
      <path d="M250 412 H57 V55 H859 V412 H666" fill="none" stroke="var(--brand-purple)" stroke-width="5"/>
      <polygon points="250,409.5 256,414.5 250,414.5" fill="var(--brand-purple)"/>
      <polygon points="666,409.5 660,414.5 666,414.5" fill="var(--brand-purple)"/>
    </svg>
    <h1 class="company-name">Tovane and Partners<span class="trademark">TM</span></h1>
    <div class="person">
      <p class="person-name">Dan Moskel</p>
      <p class="person-title">President</p>
    </div>
    <div class="divider"></div>
    <ul class="contact-list">
      <li class="contact-item">
        <svg class="contact-icon" viewBox="0 0 20 20" aria-label="Office phone">
          <rect x="0" y="0" width="20" height="20" fill="var(--ink)"/>
          <path d="M4 8 Q10 3 16 8 L14 10 L12 8 H8 L6 10 Z" fill="#fff"/>
          <rect x="6" y="11" width="8" height="5" fill="#fff"/>
        </svg>
        <span>724-555-0193</span>
      </li>
      <li class="contact-item">
        <svg class="contact-icon" viewBox="0 0 20 20" aria-label="Cell phone">
          <rect x="0" y="0" width="20" height="20" fill="var(--ink)"/>
          <rect x="6" y="3" width="8" height="14" fill="#fff"/>
          <rect x="7.5" y="5" width="5" height="4" fill="var(--ink)"/>
          <rect x="7.5" y="11" width="5" height="4" fill="var(--ink)"/>
        </svg>
        <span>724-555-0147</span>
      </li>
    </ul>
    <p class="address">5173 Wexmoor Lane, Hermitage PA 16203-4419</p>
    <div class="footer-band">
      <span class="email">danmoskel@tovanepartners-example.com</span>
      <span class="footer-sep" aria-hidden="true"></span>
      <span class="website">TovanePartners-example.com</span>
    </div>
  </section>

  <section class="card card-back" aria-label="Card back">
    <h2 class="company-name">Tovane and Partners<span class="trademark">TM</span></h2>
  </section>
</main>
</body>
</html>
```